ecommerce news podcast artwork

Podcast cover art for a podcast featuring daily news and events around ecommerce product businesses.

text to be: VORLA BEAT
optional third line of text with smaller font: Podcast

looking for something that pops with a medium to light blue background. text can be in white/red/orange colors. prefer solid colors for text, but background can vary.
I'm really open to other ideas too, sometimes you don't know what you want until you see it.

Target Market(s)

ecommerce business owners, managers

Industry/Entity Type

news, business, ecommerce

Font styles to use
Sans Serif

Colors
0054AA
0677BA
7BADD7
CADEEF
E8F1F8
0094D4
00A9DD
6FCCEA
C7EBF8
E9F6FB
F0912C
F2A743
F7CA91
FBE8D2
FDF5EE
EB3D1F
EC4F4E
F09395
F8D3D4
FCEDEE

Requirements
Must have
• text: VORLA BEAT
Should not have
• no microphones, headsets/headphones, speakers, or other props like that.

```html
<!DOCTYPE html>
<html lang="en">
<head>
<meta charset="utf-8">
<title>Vorla Beat Podcast Cover</title>
<link rel="stylesheet" href="https://fonts.googleapis.com/css2?family=Poppins:wght@500;600&display=swap">
<style>
  :root {
    --sky-light: #3aaadf;
    --sky-mid: #2a93d2;
    --ocean: #0677ba;
    --navy: #0a45a0;
    --white: #ffffff;
  }
  * { margin: 0; padding: 0; box-sizing: border-box; }
  html, body {
    width: 1200px;
    height: 1200px;
    overflow: hidden;
    background: var(--white);
  }
  .cover {
    position: relative;
    width: 1200px;
    height: 1200px;
    overflow: hidden;
    font-family: "Poppins", sans-serif;
    color: var(--white);
    background:
      radial-gradient(ellipse 900px 500px at 20% 35%, rgba(120, 210, 240, 0.3), transparent 70%),
      linear-gradient(170deg, var(--sky-mid) 0%, var(--sky-light) 30%, var(--sky-mid) 55%, var(--ocean) 72%, var(--navy) 100%);
  }
  .cover__sheen {
    position: absolute;
    inset: 0;
    width: 1200px;
    height: 1200px;
  }
  .show-name {
    position: absolute;
    top: 500px;
    left: 0;
    width: 1200px;
    text-align: center;
    font-size: 116px;
    font-weight: 600;
    letter-spacing: 0.1em;
    text-indent: 0.1em;
    line-height: 1.2;
    white-space: nowrap;
  }
  .tagline {
    position: absolute;
    top: 1056px;
    left: 164px;
    width: 872px;
    display: flex;
    justify-content: space-between;
    font-size: 34px;
    font-weight: 500;
    line-height: 1.2;
  }
</style>
</head>
<body>
  <main class="cover">
    <svg class="cover__sheen" viewBox="0 0 1200 1200" aria-hidden="true">
      <defs>
        <linearGradient id="sheenBand" x1="0" y1="0" x2="1" y2="1">
          <stop offset="0" stop-color="#6fccea" stop-opacity="0"/>
          <stop offset="0.5" stop-color="#6fccea" stop-opacity="0.15"/>
          <stop offset="1" stop-color="#6fccea" stop-opacity="0"/>
        </linearGradient>
      </defs>
      <path d="M0 650 C 250 450, 450 200, 700 0 L 900 0 C 650 250, 400 550, 0 900 Z" fill="url(#sheenBand)"/>
    </svg>

    <h1 class="show-name">VORLA BEAT</h1>
    <p class="tagline" aria-label="Podcast">
      <span>P</span><span>O</span><span>D</span><span>C</span><span>A</span><span>S</span><span>T</span>
    </p>
  </main>
</body>
</html>
```